Design a For Sale sign board and Direction Sign Board.
Attached is an example of what i am thinking but am happy to look at any options.
Colours are to be ""bright Orange"on white and in reverse as well.

Logo Text

Logo id Brookvale & Co Real Estate.

```html
<!DOCTYPE html>
<html lang="en">
<head>
<meta charset="utf-8">
<title>Brookvale &amp; Co Real Estate – Sign Boards</title>
<link rel="stylesheet" href="https://fonts.googleapis.com/css2?family=Saira+Expanded:wght@600;700;800&display=swap">
<style>
  :root {
    --backdrop: #36454c;
    --orange: #fc5210;
    --lime: #c4e804;
    --white: #ffffff;
    --sign-font: "Saira Expanded", sans-serif;
  }
  * { margin: 0; padding: 0; box-sizing: border-box; }
  html, body {
    width: 1200px;
    height: 831px;
    overflow: hidden;
    background: var(--backdrop);
  }
  .sheet {
    position: relative;
    width: 1200px;
    height: 831px;
  }
  .sign {
    position: absolute;
    width: 524px;
    height: 347px;
    border-radius: 4px;
    box-shadow: 10px 12px 18px rgba(0, 0, 0, 0.45);
    font-family: var(--sign-font);
    text-align: center;
    color: var(--ink);
    background: var(--paper);
  }
  .sign--top-left    { left: 54px;  top: 53px; }
  .sign--top-right   { left: 622px; top: 53px; }
  .sign--bottom-left { left: 54px;  top: 432px; }
  .sign--bottom-right{ left: 622px; top: 432px; }

  .sign--orange-solid { --paper: var(--orange); --ink: var(--white); }
  .sign--lime-solid   { --paper: var(--lime);   --ink: var(--white); }
  .sign--orange-on-white { --paper: var(--white); --ink: var(--orange); }
  .sign--lime-on-white   { --paper: var(--white); --ink: var(--lime); }

  .sign__frame {
    position: absolute;
    left: 25px;
    top: 26px;
    width: 474px;
    height: 295px;
    border: 6px solid var(--ink);
  }
  .sign--orange-on-white .sign__frame,
  .sign--lime-on-white .sign__frame {
    border-width: 8px;
  }

  .sign__brand {
    position: absolute;
    left: 0;
    right: 0;
    top: 62px;
    font-weight: 700;
    line-height: 1;
    letter-spacing: -0.5px;
  }
  .sign__brand-name {
    display: block;
    font-size: 31px;
  }
  .sign__brand-trade {
    display: block;
    margin-top: 8px;
    font-size: 20px;
  }

  .sign__agent {
    position: absolute;
    left: 0;
    right: 0;
    top: 174px;
    font-size: 43px;
    font-weight: 800;
    line-height: 1;
    letter-spacing: 1px;
  }
  .sign__phone {
    position: absolute;
    left: 0;
    right: 0;
    top: 224px;
    font-size: 43px;
    font-weight: 600;
    line-height: 1;
    letter-spacing: 3px;
  }
</style>
</head>
<body>
<main class="sheet">

  <section class="sign sign--top-left sign--orange-solid">
    <div class="sign__frame"></div>
    <p class="sign__brand"><span class="sign__brand-name">Brookvale &amp; Co</span><span class="sign__brand-trade">Real Estate</span></p>
    <p class="sign__agent">DANIEL MARSH</p>
    <p class="sign__phone">0400 555 182</p>
  </section>

  <section class="sign sign--top-right sign--lime-solid">
    <div class="sign__frame"></div>
    <p class="sign__brand"><span class="sign__brand-name">Brookvale &amp; Co</span><span class="sign__brand-trade">Real Estate</span></p>
    <p class="sign__agent">DANIEL MARSH</p>
    <p class="sign__phone">0400 555 182</p>
  </section>

  <section class="sign sign--bottom-left sign--orange-on-white">
    <div class="sign__frame"></div>
    <p class="sign__brand"><span class="sign__brand-name">Brookvale &amp; Co</span><span class="sign__brand-trade">Real Estate</span></p>
    <p class="sign__agent">DANIEL MARSH</p>
    <p class="sign__phone">0400 555 182</p>
  </section>

  <section class="sign sign--bottom-right sign--lime-on-white">
    <div class="sign__frame"></div>
    <p class="sign__brand"><span class="sign__brand-name">Brookvale &amp; Co</span><span class="sign__brand-trade">Real Estate</span></p>
    <p class="sign__agent">DANIEL MARSH</p>
    <p class="sign__phone">0400 555 182</p>
  </section>

</main>
</body>
</html>
```